2 Page Business Flyer for Finance Business

Need a two page flyer created for a finance business. Lots of text and needs to fit on two pages.

Corporate business/banking look and feel. Not too many large images. Lots of white space, clean design. Attached is color palette and the text contents of the flyer.

```html
<!DOCTYPE html>
<html lang="en">
<head>
<meta charset="utf-8">
<title>Vanilla Option Flyer</title>
<link href="https://fonts.googleapis.com/css2?family=Jost:wght@400;500;600;700&family=Didact+Gothic&display=swap" rel="stylesheet">
<style>
:root{
  --teal:#4dbfa5;
  --teal-dark:#3aa78e;
  --navy:#241f5c;
  --ink:#3b3b46;
  --paper:#ffffff;
  --backdrop:#e7e5e2;
  --photo-a:#1d2b4a;
  --photo-b:#8fa1b8;
}
*{box-sizing:border-box;margin:0;padding:0}
html,body{width:1200px;height:817px;overflow:hidden}
body{background:var(--backdrop);font-family:"Didact Gothic",sans-serif;color:var(--ink);position:relative}
.page{position:absolute;top:27px;width:540px;height:763px;background:var(--paper);overflow:hidden;box-shadow:0 4px 18px rgba(0,0,0,.18)}
.page--front{left:40px}
.page--back{left:620px}
.abs{position:absolute}
.hero-photo{left:0;top:0;width:540px;height:240px;background:linear-gradient(135deg,var(--photo-a) 0%,#3d5577 45%,var(--photo-b) 100%)}
.bands{left:0;width:540px}
.shield{width:120px;height:130px}
.headline-lead{left:34px;top:258px;font-family:"Jost",sans-serif;font-weight:700;font-size:36px;color:var(--teal);letter-spacing:.5px}
.headline-main{left:34px;top:300px;font-family:"Jost",sans-serif;font-weight:700;font-size:21px;color:var(--navy)}
.body-copy{font-size:7.2px;line-height:1.45;color:var(--ink)}
.lead-copy{left:34px;top:336px;width:470px}
.key-statement{left:34px;top:374px;width:470px;font-family:"Jost",sans-serif;font-weight:700;font-size:9.5px;line-height:1.35;color:var(--navy)}
.navy-band{background:var(--navy);color:#fff}
.buyer-band{left:0;top:404px;width:540px;height:24px;padding:5px 34px;font-family:"Jost",sans-serif;font-weight:600;font-size:10.5px}
.step-list{left:34px;top:438px;list-style:none}
.step-list li{display:flex;align-items:center;gap:10px;font-size:10px;margin-bottom:6px;color:var(--ink)}
.num{width:13px;height:13px;border-radius:50%;background:var(--navy);color:#fff;font-family:"Jost",sans-serif;font-size:7.5px;font-weight:600;display:flex;align-items:center;justify-content:center;flex:none}
.example-pill{left:34px;top:523px;padding:5px 20px;border-radius:14px;background:var(--teal);color:#fff;font-family:"Jost",sans-serif;font-weight:700;font-size:14px}
.example-copy{left:34px;top:558px;width:470px;font-size:6.6px}
.footer-call{font-family:"Jost",sans-serif;color:#fff;font-size:16px;font-weight:500;display:flex;align-items:center;gap:10px}
.footer-call strong{font-weight:500;font-size:15px}
.footer-visit{font-family:"Jost",sans-serif;color:#fff;font-size:12px;display:flex;align-items:center;gap:8px}
.footer-visit .url{font-size:12.5px}
.tab{left:34px;padding:3px 12px;background:var(--teal);color:#fff;font-family:"Jost",sans-serif;font-weight:600;font-size:9.5px;border-radius:0 10px 10px 0}
.dot-list{list-style:none;left:44px}
.dot-list li{font-size:7.6px;line-height:1.55}
.dot-list li::before{content:"·";margin-right:4px;font-weight:700}
.num-list{list-style:none;left:44px}
.num-list li{display:flex;align-items:center;gap:8px;font-size:8px;margin-bottom:4px}
.num-list .num{width:11px;height:11px;font-size:6.5px}
.wide-band{left:0;width:540px;padding:8px 34px}
.tick-list{list-style:none;left:44px;top:525px}
.tick-list li{display:flex;align-items:center;gap:9px;font-size:8.4px;margin-bottom:5px}
.tick{width:11px;height:11px;border-radius:50%;background:var(--navy);flex:none;display:flex;align-items:center;justify-content:center}
</style>
</head>
<body>

<!-- Front page -->
<section class="page page--front">
  <div class="abs hero-photo" role="img" aria-label="Photograph of business people reviewing financial charts on a tablet and paper reports"></div>
  <svg class="abs bands" style="top:200px" width="540" height="70" viewBox="0 0 540 70">
    <polygon points="0,40 540,10 540,40 0,70" fill="#fff"/>
    <polygon points="0,28 540,0 540,16 0,46" fill="var(--navy)"/>
    <polygon points="0,46 300,30 300,33 0,54" fill="var(--teal)"/>
    <polygon points="0,54 540,24 540,70 0,70" fill="#fff"/>
  </svg>
  <svg class="abs shield" style="left:390px;top:135px" viewBox="0 0 120 130" role="img" aria-label="Shield framed illustration of a hand holding a glowing dollar coin">
    <defs><linearGradient id="shieldFill1" x1="0" y1="0" x2="0" y2="1"><stop offset="0" stop-color="#1f4b6e"/><stop offset="1" stop-color="#0f2740"/></linearGradient></defs>
    <path d="M60 4 L112 18 Q114 80 60 126 Q6 80 8 18 Z" fill="url(#shieldFill1)" stroke="var(--teal)" stroke-width="4"/>
  </svg>

  <div class="abs headline-lead">How does a</div>
  <div class="abs headline-main">Vanilla Option contract work?</div>

  <p class="abs body-copy lead-copy">The buyer of a vanilla option receives protection against an adverse movement in the exchange rate while allowing full participation in a beneficial move. At no time is the buyer of a vanilla option obligated to exercise the option and transact the currencies, therefore providing flexibility in cases where the requirement to purchase foreign currency is not certain.</p>

  <p class="abs key-statement">A buyer of vanilla options is required to pay a premium (like an insurance premium) for the right, but not the obligation, to exchange currency at a predetermined rate on a predetermined date.</p>

  <div class="abs navy-band buyer-band">A buyer of vanilla options will:</div>

  <ol class="abs step-list">
    <li><span class="num">1</span>Set a protection rate which will be your worst-case scenario at expiry</li>
    <li><span class="num">2</span>Determine the amount of currency you wish to protect</li>
    <li><span class="num">3</span>Choose an expiry date for the contract</li>
    <li><span class="num">4</span>Calculate the premium you are required to pay</li>
  </ol>

  <div class="abs example-pill">Let’s look at an example: You are an importer.</div>

  <p class="abs body-copy example-copy">Your construction company has bid on a project that, if successful, will require you to import materials from the United States to use in construction. You have used today’s pricing of materials in calculating your bid and want to protect against an adverse move in the US dollar exchange rate from eroding your margin if your bid is chosen. For the project you choose to buy a vanilla call which will protect you from a rise in the USD/CAD exchange rate above your protection rate. You choose to buy protection on $500,000 USD, with a protection rate (strike rate) of 1.3300 expiring 3 months from now. You are required to pay a premium, which in this case is calculated to be 1.8%, or 11,970 CAD. If your bid is successful and the exchange rate is below your protection rate at expiration, you have no obligation relating to the vanilla call and you are free to buy USD at the cheaper spot rate. If the exchange rate is above your protection rate, you may exercise your right to purchase your USD at the protection rate and thereby claiming your insurance policy. If your bid is not successful, you have no obligation to buy the USD. However, if at expiry the exchange rate is above the protection rate, you may still exercise and simultaneously sell back at the prevailing spot rate, thereby recouping some or all of the premium paid. Alternatively, if you find out your bid was not successful with time still left until expiration, you may sell your option back into the market in the case that it still has residual value, which will depend on various market factors.</p>

  <svg class="abs bands" style="top:672px" width="540" height="91" viewBox="0 0 540 91">
    <polygon points="0,30 330,30 318,91 0,91" fill="var(--teal)"/>
    <polygon points="340,0 540,0 540,91 310,91" fill="var(--navy)"/>
    <polygon points="0,24 335,24 333,30 0,30" fill="var(--navy)"/>
  </svg>
  <div class="abs footer-call" style="left:28px;top:725px">call us:
    <svg width="13" height="13" viewBox="0 0 24 24"><path fill="#fff" d="M6.6 10.8a15.1 15.1 0 0 0 6.6 6.6l2.2-2.2c.3-.3.7-.4 1-.2 1.1.4 2.3.6 3.6.6.6 0 1 .4 1 1V20c0 .6-.4 1-1 1A17 17 0 0 1 3 4c0-.6.4-1 1-1h3.5c.6 0 1 .4 1 1 0 1.3.2 2.5.6 3.6.1.3 0 .7-.2 1z"/></svg>
    <strong>033-555 010 246</strong></div>
  <div class="abs footer-visit" style="left:360px;top:686px">visit us:
    <svg width="11" height="11" viewBox="0 0 24 24"><circle cx="12" cy="12" r="10" fill="none" stroke="#fff" stroke-width="2"/><path d="M2 12h20M12 2c3 3 3 17 0 20M12 2c-3 3-3 17 0 20" fill="none" stroke="#fff" stroke-width="1.6"/></svg>
    <span class="url">www.harbourlinefx.com</span></div>
</section>

<!-- Back page -->
<section class="page page--back">
  <svg class="abs bands" style="top:0" width="540" height="130" viewBox="0 0 540 130">
    <polygon points="120,70 480,70 480,78 20,112" fill="var(--navy)"/>
    <polygon points="0,98 300,78 300,82 0,112" fill="var(--teal)"/>
    <polygon points="0,112 300,82 0,130" fill="var(--teal)" opacity=".25"/>
  </svg>
  <svg class="abs shield" style="left:398px;top:8px" viewBox="0 0 120 130" role="img" aria-label="Shield framed photograph of a businessman reviewing printed charts at a desk">
    <defs><linearGradient id="shieldFill2" x1="0" y1="0" x2="1" y2="1"><stop offset="0" stop-color="#e8ecef"/><stop offset="1" stop-color="#5b6470"/></linearGradient></defs>
    <path d="M60 4 L112 18 Q114 80 60 126 Q6 80 8 18 Z" fill="url(#shieldFill2)" stroke="var(--teal)" stroke-width="4"/>
  </svg>

  <div class="abs tab" style="top:138px">Characteristics</div>
  <ul class="abs dot-list" style="top:160px">
    <li>You are looking for a straight-forward hedging solution</li>
    <li>You want to receive full benefit from an appreciation of the currency you are exposed to</li>
    <li>You are comfortable receiving protection at the strike rate of the option</li>
    <li>You are willing to pay the non-refundable premium</li>
  </ul>

  <div class="abs tab" style="top:222px">Advantages</div>
  <ol class="abs num-list" style="top:244px">
    <li><span class="num">1</span>You hedge your foreign currency exposure at a predefined hedge rate</li>
    <li><span class="num">2</span>You can choose the hedge rate that suits your budget requirements</li>
    <li><span class="num">3</span>Provides the ability to fully participate in a favourable exchange rate move</li>
    <li><span class="num">4</span>You can choose from most major currency pairs to meet your needs</li>
  </ol>

  <div class="abs tab" style="top:312px">Risks</div>
  <ol class="abs num-list" style="top:333px">
    <li><span class="num">1</span>Premium paid is non-refundable and remains your only obligation when</li>
    <li><span class="num">2</span>buying vanilla options</li>
  </ol>

  <div class="abs navy-band" style="left:180px;top:366px;width:360px;height:22px"></div>
  <div class="abs tab" style="top:366px;padding:4px 14px">Why use Vanilla Options?</div>
  <p class="abs body-copy" style="left:34px;top:394px;width:470px">Vanilla options are often compared to an insurance product. The buyer pays a non-refundable premium for the right, but not the obligation to trade currency in the future at the protection rate of the option. This product allows you to participate in a beneficial move to an unlimited extent, which will be the most advantageous outcome, if the exchange rate moves in your favour enough to more than offset the premium paid for the option.</p>

  <div class="abs navy-band wide-band" style="top:440px;height:76px;padding-top:32px">
    <p class="body-copy" style="color:#fff;font-size:7.4px">The cost of an option is defined by the premium that is required to be paid in order to enter into the contract. Premiums are calculated using the industry standard formulas based upon the Black Scholes model. The most important variables in the option pricing formulas include the following:</p>
  </div>
  <div class="abs tab" style="top:432px;padding:5px 16px;font-size:10px">What determines the price of a Vanilla Option?</div>

  <ul class="abs tick-list">
    <li><span class="tick"><svg width="7" height="7" viewBox="0 0 10 10"><path d="M1.5 5.2l2.2 2.2 4.8-5" fill="none" stroke="#fff" stroke-width="1.8"/></svg></span>The current market Spot Rate.</li>
    <li><span class="tick"><svg width="7" height="7" viewBox="0 0 10 10"><path d="M1.5 5.2l2.2 2.2 4.8-5" fill="none" stroke="#fff" stroke-width="1.8"/></svg></span>Market volatility – the higher the volatility, the higher the premium.</li>
    <li><span class="tick"><svg width="7" height="7" viewBox="0 0 10 10"><path d="M1.5 5.2l2.2 2.2 4.8-5" fill="none" stroke="#fff" stroke-width="1.8"/></svg></span>The Term of the Option – a longer term typically results in a higher premium.</li>
    <li><span class="tick"><svg width="7" height="7" viewBox="0 0 10 10"><path d="M1.5 5.2l2.2 2.2 4.8-5" fill="none" stroke="#fff" stroke-width="1.8"/></svg></span>The Strike Rate – the closer to being ITM the protection rate is, the higher the premium.</li>
    <li><span class="tick"><svg width="7" height="7" viewBox="0 0 10 10"><path d="M1.5 5.2l2.2 2.2 4.8-5" fill="none" stroke="#fff" stroke-width="1.8"/></svg></span>The interest rate differential of the two currencies involved.</li>
    <li><span class="tick"><svg width="7" height="7" viewBox="0 0 10 10"><path d="M1.5 5.2l2.2 2.2 4.8-5" fill="none" stroke="#fff" stroke-width="1.8"/></svg></span>Style – European or American, or whether the option can be exercised prior to expiration</li>
  </ul>

  <svg class="abs bands" style="top:622px" width="540" height="141" viewBox="0 0 540 141">
    <polygon points="0,0 540,0 540,10 0,10" fill="var(--teal)"/>
    <polygon points="0,10 540,10 540,58 0,58" fill="var(--navy)"/>
    <polygon points="300,62 540,62 540,88 290,88" fill="var(--teal)"/>
    <polygon points="0,96 300,96 292,141 0,141" fill="var(--navy)"/>
  </svg>
  <p class="abs body-copy" style="left:34px;top:636px;width:470px;color:#fff">An option can either a European (meaning that they can only be exercised on the expiry date), or American (meaning that they can be exercised at any time prior to expiration). We normally deal in European options however, we do offer American options under certain circumstances and when specific delivery terms are agreed upon between us and the customer.</p>
  <div class="abs footer-visit" style="left:318px;top:688px">visit us:
    <svg width="11" height="11" viewBox="0 0 24 24"><circle cx="12" cy="12" r="10" fill="none" stroke="#fff" stroke-width="2"/><path d="M2 12h20M12 2c3 3 3 17 0 20M12 2c-3 3-3 17 0 20" fill="none" stroke="#fff" stroke-width="1.6"/></svg>
    <span class="url">www.harbourlinefx.com</span></div>
  <div class="abs footer-call" style="left:28px;top:732px">call us:
    <svg width="13" height="13" viewBox="0 0 24 24"><path fill="#fff" d="M6.6 10.8a15.1 15.1 0 0 0 6.6 6.6l2.2-2.2c.3-.3.7-.4 1-.2 1.1.4 2.3.6 3.6.6.6 0 1 .4 1 1V20c0 .6-.4 1-1 1A17 17 0 0 1 3 4c0-.6.4-1 1-1h3.5c.6 0 1 .4 1 1 0 1.3.2 2.5.6 3.6.1.3 0 .7-.2 1z"/></svg>
    <strong>033-555 010 246</strong></div>
</section>

</body>
</html>
```